Colin Marsh Optometry "we are moving" - to be used as a business card size magnet

Our optometry business "Colin Marsh Optometry" is moving location at the end of 2017. We plan to have business card size magnets printed to hand to our current customers to remind them that we are moving at the end of this year. We would like a clean, simple design that uses our logo and colour branding (see uploaded business card) with our new address "42 Carrow Lane Kelbridge" our phone number "6827 1054" and "same great people, same great service" and "just next to the Silver Lark Dentist".

```html
<!DOCTYPE html>
<html lang="en">
<head>
<meta charset="utf-8">
<title>Colin Marsh Optometry – We Are Moving Magnet</title>
<link href="https://fonts.googleapis.com/css2?family=Nunito:wght@400;700&display=swap" rel="stylesheet">
<style>
  :root {
    --page: #ffffff;
    --card: #4f3c55;
    --ink: #ffffff;
  }
  * { box-sizing: border-box; margin: 0; padding: 0; }
  html, body {
    width: 1200px;
    height: 825px;
    overflow: hidden;
    background: var(--page);
  }
  .canvas {
    position: relative;
    width: 1200px;
    height: 825px;
  }
  .magnet {
    position: absolute;
    left: 403px;
    top: 300px;
    width: 391px;
    height: 239px;
    background: var(--card);
    color: var(--ink);
    font-family: "Nunito", sans-serif;
    font-weight: 700;
    text-align: center;
    overflow: hidden;
  }
  .brand {
    position: absolute;
    top: 32px;
    left: 0;
    right: 0;
    height: 30px;
    display: flex;
    justify-content: center;
    align-items: center;
    gap: 10px;
  }
  .brand-mark {
    width: 14px;
    height: 14px;
    background: var(--ink);
  }
  .brand-name {
    font-size: 25px;
    font-weight: 700;
    letter-spacing: -0.3px;
    line-height: 1;
  }
  .address {
    position: absolute;
    top: 110px;
    left: 0;
    right: 0;
    font-size: 14px;
    line-height: 22px;
    letter-spacing: -0.3px;
  }
  .tagline {
    position: absolute;
    top: 167px;
    left: 0;
    right: 0;
    font-size: 14.5px;
    line-height: 20px;
    letter-spacing: -0.3px;
  }
  .landmark {
    position: absolute;
    top: 207px;
    left: 0;
    right: 0;
    font-size: 11px;
    line-height: 14px;
    letter-spacing: -0.2px;
  }
</style>
</head>
<body>
  <main class="canvas">
    <section class="magnet">
      <div class="brand">
        <span class="brand-mark" aria-hidden="true"></span>
        <span class="brand-name">Colin Marsh Optometry</span>
      </div>
      <p class="address">42 Carrow Lane Kelbridge<br>76827 1054</p>
      <p class="tagline">same great people, same great service</p>
      <p class="landmark">just next to the Silver Lark Dentist</p>
    </section>
  </main>
</body>
</html>
```